Business Card Design

We need a business card design for a new company called Velmar Joinery. We make, design and install all joinery.
We want a classy business card which is not to busy, we want a double sided card with just the logo on one side and all the required information on the other. We are a partnership so would like cards with both names and numbers. We would like to see a design which blends in with our logo and really makes it pop.

Reason: I would like my logo displayed on the business card please.

Industry/Entity Type

Business

Contact Information for Business Card

Name- Dean Velmar Phone Number- 047318562
Name- Luke Velmar Phone Number- 0418265931 E-mail- velmarjoinery@examplemail.net
License Number- 583920k Company Name- Velmar Joinery ABN-47 508 293 614

Colors
0456a4
ffffff

```html
<!DOCTYPE html>
<html lang="en">
<head>
<meta charset="utf-8">
<title>Velmar Joinery – Business Card</title>
<link href="https://fonts.googleapis.com/css2?family=Source+Sans+3:wght@400;600&display=swap" rel="stylesheet">
<style>
  :root {
    --brand-blue: #0456a4;
    --accent-blue: #1a7bc4;
    --card-white: #ffffff;
    --card-black: #0a0a0a;
    --ink: #1d1d1d;
    --ink-soft: #555555;
    --backdrop: #d9d9d9;
  }
  * { margin: 0; padding: 0; box-sizing: border-box; }
  html, body { width: 1200px; height: 675px; overflow: hidden; }
  body {
    background: var(--backdrop);
    font-family: "Source Sans 3", "Myriad Pro", sans-serif;
    position: relative;
  }
  .card {
    position: absolute;
    top: 187px;
    width: 510px;
    height: 300px;
    overflow: hidden;
    box-shadow: 0 6px 18px rgba(0,0,0,0.25);
  }
  .card--front { left: 60px; background: var(--card-black); }
  .card--back { left: 630px; background: var(--card-white); }

  .wordmark {
    position: absolute;
    display: flex;
    align-items: center;
    gap: 10px;
    font-weight: 600;
    letter-spacing: 1px;
    white-space: nowrap;
  }
  .wordmark__square {
    width: 26px; height: 26px;
    background: var(--brand-blue);
  }
  .card--front .wordmark {
    left: 50%; top: 50%;
    transform: translate(-50%, -50%);
    font-size: 30px;
    color: var(--card-white);
  }
  .card--back .wordmark {
    right: 28px; top: 46px;
    font-size: 28px;
    color: var(--ink);
  }

  .contacts {
    position: absolute;
    left: 30px; top: 104px;
    color: var(--ink-soft);
  }
  .person { position: relative; margin-bottom: 8px; }
  .person__marker {
    position: absolute;
    left: -30px; top: 5px;
    width: 10px; height: 10px;
    background: var(--accent-blue);
  }
  .person__name { font-size: 18px; line-height: 20px; color: var(--ink); }
  .person__surname { color: var(--accent-blue); }
  .contact-line {
    display: flex; align-items: center; gap: 6px;
    font-size: 12.5px; line-height: 16px;
  }
  .contact-line svg { width: 12px; height: 12px; fill: var(--accent-blue); flex: none; }
  .email { margin-top: 4px; }
  .licence { margin-top: 3px; font-size: 12.5px; }
  .licence__number { color: var(--accent-blue); }

  .company-footer {
    position: absolute;
    right: 28px; bottom: 32px;
    text-align: right;
    font-size: 13.5px; line-height: 17px;
    color: var(--ink-soft);
  }
  .base-band {
    position: absolute;
    left: 0; right: 0; bottom: 0;
    height: 14px;
    display: flex;
  }
  .base-band__dark { width: 44%; background: var(--card-black); }
  .base-band__blue { flex: 1; background: var(--accent-blue); }
</style>
</head>
<body>

<section class="card card--front" aria-label="Card front">
  <div class="wordmark"><span class="wordmark__square"></span>VELMAR JOINERY</div>
</section>

<section class="card card--back" aria-label="Card back">
  <div class="wordmark"><span class="wordmark__square"></span>VELMAR JOINERY</div>

  <div class="contacts">
    <div class="person">
      <span class="person__marker"></span>
      <div class="person__name">Dean<span class="person__surname">Velmar</span></div>
      <div class="contact-line">
        <svg viewBox="0 0 24 24"><path d="M6.6 10.8a15.1 15.1 0 0 0 6.6 6.6l2.2-2.2a1 1 0 0 1 1-.25 11.4 11.4 0 0 0 3.6.57 1 1 0 0 1 1 1V20a1 1 0 0 1-1 1A17 17 0 0 1 3 4a1 1 0 0 1 1-1h3.5a1 1 0 0 1 1 1c0 1.25.2 2.45.57 3.57a1 1 0 0 1-.25 1z"/></svg>
        047318562
      </div>
    </div>
    <div class="person">
      <span class="person__marker"></span>
      <div class="person__name">Luke<span class="person__surname">Velmar</span></div>
      <div class="contact-line">
        <svg viewBox="0 0 24 24"><path d="M6.6 10.8a15.1 15.1 0 0 0 6.6 6.6l2.2-2.2a1 1 0 0 1 1-.25 11.4 11.4 0 0 0 3.6.57 1 1 0 0 1 1 1V20a1 1 0 0 1-1 1A17 17 0 0 1 3 4a1 1 0 0 1 1-1h3.5a1 1 0 0 1 1 1c0 1.25.2 2.45.57 3.57a1 1 0 0 1-.25 1z"/></svg>
        0418265931
      </div>
    </div>
    <div class="contact-line email">
      <svg viewBox="0 0 24 24"><path d="M2 5h20v14H2z M3.5 6.5 12 13l8.5-6.5" fill="none" stroke="#1a7bc4" stroke-width="2"/></svg>
      velmarjoinery@examplemail.net
    </div>
    <div class="licence">License Number: <span class="licence__number">583920k</span></div>
  </div>

  <div class="company-footer">
    Velmar Joinery<br>
    ABN-47 508 293 614
  </div>

  <div class="base-band">
    <span class="base-band__dark"></span>
    <span class="base-band__blue"></span>
  </div>
</section>

</body>
</html>
```